Real Estate Seller Financing Postcard

I need a postcard that lays out these options contained in the notes that grabs attention, explains the two options easily and is eye-catching. The front needs to have the percentages on it and information about it and on the other side One side exact Text is:
"Monthly income without tenant headaches" in big letters. Also on front "Get
110%
add an "or"
160% of market value for your property. ". The percentages should be displayed and that is not to be a sentence of text. Other side text: I need bullets points for these "Formal protection as a lien holder against home
No commission or closing cost
Fast closings possible
Property taken as is so no repairs.

Add to the top of the back in "It’s simple. I am a new investor without down payment capital who still want to double our portfolio this year to grow our portfolio."
Here are the two options that are to be the largest part of the back
Option 1, you can receive 80% now cash and 30% over a short period of time including interest.

Option 2, where act like a bank allowing you to make 150% if you finance the whole property(ies). No gimmicks and surprises, just simple unconventional financing.

Include Logo Somewhere

Target Market(s)

Property Owners Wanting to Sell Their Property

Industry/Entity Type

Real Estate Investing

Requirements
Must have
• The options promiment and each side with its respective information. Must have logo somewhere
Nice to have
• The options in color other than black.
Should not have
• A picture of money on the front. Any other image is okay.

```html
<!DOCTYPE html>
<html lang="en">
<head>
<meta charset="utf-8">
<title>Meridian Real Estate Group – Seller Financing Postcard</title>
<link href="https://fonts.googleapis.com/css2?family=Bebas+Neue&family=Open+Sans:wght@600;700;800&family=PT+Sans:wght@400;700&display=swap" rel="stylesheet">
<style>
  :root {
    --brand-blue: #22408a;
    --band-fade: #9096cc;
    --accent-orange: #f5a623;
    --ink: #161616;
    --paper: #ffffff;
    --soft-grey: #e8e8e8;
    --rule-grey: #b9b9b9;
    --backdrop: #e4e4e4;
  }
  * { box-sizing: border-box; margin: 0; padding: 0; }
  html, body {
    width: 893px; height: 1200px; overflow: hidden;
    background: var(--backdrop);
  }
  .postcard {
    position: absolute; left: 58px; width: 765px; height: 510px;
    background: var(--paper); overflow: hidden;
  }
  .postcard--front { top: 62px; }
  .postcard--back { top: 610px; }
  .postcard__shapes { position: absolute; inset: 0; }

  .brand { position: absolute; display: flex; align-items: center; gap: 10px; }
  .brand__mark {
    border: 2px solid var(--brand-blue); border-radius: 50%; flex: none;
  }
  .brand__name {
    font-family: "Open Sans", sans-serif; font-weight: 700; color: var(--brand-blue);
    line-height: 1.05;
  }
  .brand__name span { display: block; }
  .brand__name .brand__line-main { font-size: 25px; letter-spacing: 0.5px; }
  .brand__name .brand__line-sub { font-size: 10px; letter-spacing: 0.4px; }
  .postcard--front .brand { left: 55px; top: 57px; }
  .postcard--front .brand__mark { width: 58px; height: 58px; }
  .postcard--back .brand { left: 442px; top: 420px; }
  .postcard--back .brand__mark { width: 55px; height: 55px; }

  .headline { position: absolute; left: 52px; top: 140px; }
  .headline__lead {
    font-family: "Open Sans", sans-serif; font-weight: 800; font-size: 19.5px;
    color: var(--ink); letter-spacing: -0.3px; line-height: 1;
  }
  .headline__big {
    font-family: "Bebas Neue", sans-serif; font-size: 60px; line-height: 0.88;
    letter-spacing: 1.5px;
  }
  .headline__big--tenant { color: var(--paper); margin-top: 9px; letter-spacing: 6px; }
  .headline__big--headaches { color: var(--accent-orange); margin-top: 2px; }

  .benefits {
    position: absolute; left: 56px; top: 286px; width: 250px; list-style: none;
    font-family: "PT Sans", sans-serif; font-size: 17.5px; color: var(--ink);
    line-height: 1.18;
    border-top: 1.5px dashed var(--rule-grey);
  }
  .benefits li {
    display: flex; gap: 4px; padding: 7px 0 6px;
    border-bottom: 1.5px dashed var(--rule-grey);
  }
  .benefits li svg { flex: none; margin-top: 6px; }
  .benefits li span { white-space: nowrap; }

  .offer-badge {
    position: absolute; left: 426px; top: 52px; width: 176px; height: 176px;
    display: flex; flex-direction: column; align-items: center; justify-content: center;
    text-align: center; font-family: "Open Sans", sans-serif; font-weight: 700;
    color: var(--paper);
  }
  .offer-badge__figure { font-size: 31px; line-height: 1; letter-spacing: -0.5px; }
  .offer-badge__or { font-size: 14px; line-height: 1.2; color: var(--accent-orange); }
  .offer-badge__note { font-size: 13px; line-height: 1.12; margin-top: 3px; }

  .pitch {
    position: absolute; left: 55px; top: 68px;
    font-family: "Open Sans", sans-serif; font-weight: 700; font-size: 17.5px;
    line-height: 1.07; color: var(--paper); letter-spacing: -0.3px;
  }
  .option {
    position: absolute; left: 52px;
    font-family: "Open Sans", sans-serif; font-weight: 700; color: var(--paper);
    letter-spacing: -0.6px;
  }
  .option--cash { top: 194px; }
  .option--cash span { display: block; white-space: nowrap; }
  .option__soft { font-size: 26px; line-height: 1.13; }
  .option__loud { font-size: 33px; line-height: 1.07; }
  .option__loud small { font-size: 26px; }
  .option--finance {
    top: 398px; width: 300px; font-size: 14.5px; line-height: 1.2; letter-spacing: -0.2px;
  }
  .option__highlight { color: var(--accent-orange); font-size: 19px; }

  .stamp-box {
    position: absolute; left: 596px; top: 54px; width: 113px; height: 127px;
    border: 1.2px solid #6e6e6e;
  }
  .address-line {
    position: absolute; left: 465px; width: 246px; height: 0;
    border-top: 1.2px solid #6e6e6e;
  }
</style>
</head>
<body>

<section class="postcard postcard--front">
  <svg class="postcard__shapes" width="765" height="510" viewBox="0 0 765 510">
    <defs>
      <linearGradient id="bandFade" x1="0" x2="1" y1="0" y2="0">
        <stop offset="0.35" stop-color="var(--brand-blue)"/>
        <stop offset="1" stop-color="var(--band-fade)"/>
      </linearGradient>
      <linearGradient id="photoTones" x1="0" x2="0" y1="0" y2="1">
        <stop offset="0" stop-color="#c9d6e2"/>
        <stop offset="0.3" stop-color="#dcc0b0"/>
        <stop offset="0.55" stop-color="#9bb27f"/>
        <stop offset="1" stop-color="#4f7b3f"/>
      </linearGradient>
    </defs>
    <circle cx="800" cy="-60" r="270" fill="var(--soft-grey)"/>
    <rect x="0" y="170" width="440" height="47" fill="url(#bandFade)"/>
    <rect x="0" y="498" width="420" height="12" fill="var(--accent-orange)"/>
    <circle cx="690" cy="428" r="356" fill="none" stroke="var(--accent-orange)" stroke-width="7"/>
    <circle cx="690" cy="432" r="348" fill="var(--paper)"/>
    <circle cx="690" cy="432" r="345" fill="url(#photoTones)" role="img"
            aria-label="Photo: an agent in a suit shaking hands with a smiling couple in front of a white house with a tiled roof"/>
    <circle cx="514" cy="140" r="88" fill="var(--brand-blue)" opacity="0.95"/>
    <circle cx="514" cy="140" r="76" fill="none" stroke="var(--paper)" stroke-width="1.3" stroke-dasharray="9 6"/>
  </svg>

  <div class="brand">
    <div class="brand__mark"></div>
    <div class="brand__name">
      <span class="brand__line-main">MERIDIAN</span>
      <span class="brand__line-sub">REAL ESTATE GROUP</span>
    </div>
  </div>

  <h1 class="headline">
    <div class="headline__lead">MONTHLY INCOME WITHOUT</div>
    <div class="headline__big headline__big--tenant">TENANT</div>
    <div class="headline__big headline__big--headaches">HEADACHES</div>
  </h1>

  <ul class="benefits">
    <li>
      <svg width="13" height="13" viewBox="0 0 13 13"><path d="M1 6.5 L5 11 L12 1" fill="none" stroke="var(--brand-blue)" stroke-width="2"/></svg>
      <span>Formal protection as a lien<br>holder against home</span>
    </li>
    <li>
      <svg width="13" height="13" viewBox="0 0 13 13"><path d="M1 6.5 L5 11 L12 1" fill="none" stroke="var(--brand-blue)" stroke-width="2"/></svg>
      <span>No commission or closing cost</span>
    </li>
    <li>
      <svg width="13" height="13" viewBox="0 0 13 13"><path d="M1 6.5 L5 11 L12 1" fill="none" stroke="var(--brand-blue)" stroke-width="2"/></svg>
      <span>Fast closings possible</span>
    </li>
    <li>
      <svg width="13" height="13" viewBox="0 0 13 13"><path d="M1 6.5 L5 11 L12 1" fill="none" stroke="var(--brand-blue)" stroke-width="2"/></svg>
      <span>Property taken as is so no<br>repairs.</span>
    </li>
  </ul>

  <div class="offer-badge">
    <span class="offer-badge__figure">110%</span>
    <span class="offer-badge__or">or</span>
    <span class="offer-badge__figure">160%</span>
    <span class="offer-badge__note">of market value<br>for your property.</span>
  </div>
</section>

<section class="postcard postcard--back">
  <svg class="postcard__shapes" width="765" height="510" viewBox="0 0 765 510">
    <circle cx="800" cy="-60" r="270" fill="var(--soft-grey)"/>
    <ellipse cx="155" cy="305" rx="295" ry="282" fill="var(--accent-orange)"/>
    <ellipse cx="152" cy="303" rx="290" ry="273" fill="var(--paper)"/>
    <ellipse cx="150" cy="300" rx="285" ry="265" fill="var(--brand-blue)"/>
    <rect x="287" y="499" width="410" height="9" fill="var(--accent-orange)"/>
  </svg>

  <p class="pitch">It’s simple. I am a new<br>investor without down<br>payment capital who still<br>want to double our<br>portfolio this year to grow<br>our portfolio.</p>

  <p class="option option--cash">
    <span class="option__soft">you can receive</span>
    <span class="option__loud">80% NOW CASH</span>
    <span class="option__loud">&amp; 30% OVER A</span>
    <span class="option__loud">SHORT PERIOD <small>of</small></span>
    <span class="option__soft">time including interest.</span>
  </p>

  <p class="option option--finance"><span class="option__highlight">OR 150%</span> – we act like a bank if you finance the whole property(ies). No gimmicks and surprises, just simple unconventional financing.</p>

  <div class="stamp-box"></div>
  <div class="address-line" style="top:284px"></div>
  <div class="address-line" style="top:336px"></div>
  <div class="address-line" style="top:389px"></div>

  <div class="brand">
    <div class="brand__mark"></div>
    <div class="brand__name">
      <span class="brand__line-main">MERIDIAN</span>
      <span class="brand__line-sub">REAL ESTATE GROUP</span>
    </div>
  </div>
</section>

</body>
</html>
```